Business Card Design for a technology company

Our current business card is outdated and stale.

We need a new look and one soon.

We're a telematics (GPS tracking) company based in Australia. Our audiences are transport and logistics company.

Target Market(s)

1. Transport and Logistics Companies
2. Food and Beverage Manufacturers
3. Concrete Businesses

Industry/Entity Type

Logistics

Contact Information for Business Card

Halvor Pinet

Font styles to use
Sans Serif

Colors
3276b5
0255a3
85acd3
cfdeed
ffffff

Requirements
Must have
• Logo
• "Premium Suppliers of Real Time Temperature Tracking"
• Contact Name
• Business Title
• Address
• Telephone
• Mobile
• Email
• Website URL
Nice to have
• Visual representation of tracking or maps.
Should not have
• Image of a satellite as currently shown

```html
<!DOCTYPE html>
<html lang="en">
<head>
<meta charset="utf-8">
<title>Halvor Pinet – Business Card</title>
<link href="https://fonts.googleapis.com/css2?family=Source+Sans+3:wght@400;600;700&family=Share+Tech+Mono&display=swap" rel="stylesheet">
<style>
  :root {
    --blue-deep: #0255a3;
    --blue: #1d4f9c;
    --blue-mid: #3276b5;
    --blue-soft: #85acd3;
    --blue-pale: #cfdeed;
    --white: #ffffff;
    --ink: #151517;
    --stage: #eceef1;
  }
  * { box-sizing: border-box; margin: 0; padding: 0; }
  html, body { width: 1200px; height: 1200px; overflow: hidden; background: var(--stage); }
  body { position: relative; font-family: "Source Sans 3", sans-serif; }

  .card {
    position: absolute; left: 190px; width: 820px; height: 500px;
    overflow: hidden; box-shadow: 0 10px 30px rgba(0,0,0,.18);
  }
  .card--front { top: 60px; background: var(--ink); }
  .card--back { top: 640px; background: var(--white); }

  .wordmark { position: absolute; font-weight: 600; white-space: nowrap; letter-spacing: -1px; }
  .card--front .wordmark {
    left: 0; right: 0; top: 200px; text-align: center;
    font-size: 86px; line-height: 1; color: var(--white);
  }
  .card--back .wordmark {
    left: 50px; top: 108px; font-size: 76px; line-height: 1; color: var(--blue-deep);
  }

  .band { position: absolute; inset: 0; }

  .person { position: absolute; right: 190px; top: 62px; text-align: right; }
  .person__name { font-size: 30px; font-weight: 700; color: var(--blue-deep); line-height: 1; }
  .person__title { font-size: 17px; font-weight: 600; color: var(--ink); margin-top: 2px; }
  .person__mark {
    position: absolute; right: -24px; top: 2px; width: 18px; height: 26px; background: var(--blue-mid);
  }

  .contacts { position: absolute; left: 40px; top: 346px; list-style: none; color: var(--white); }
  .contacts li { display: flex; align-items: center; gap: 10px; font-size: 17px; line-height: 24px; }
  .contacts svg { width: 14px; height: 14px; fill: var(--white); flex: none; }

  .web {
    position: absolute; right: 40px; top: 350px; display: flex; align-items: center; gap: 8px;
    color: var(--white); font-size: 17px;
  }
  .web svg { width: 14px; height: 14px; }

  .tagline {
    position: absolute; left: 40px; right: 40px; bottom: 20px;
    font-family: "Share Tech Mono", monospace; font-size: 21px; letter-spacing: 2px;
    color: var(--white); text-transform: uppercase; white-space: nowrap;
  }
</style>
</head>
<body>

<section class="card card--front" aria-label="Card front">
  <div class="wordmark">Halvor Pinet</div>
</section>

<section class="card card--back" aria-label="Card back">
  <svg class="band" viewBox="0 0 820 500" width="820" height="500" aria-hidden="true">
    <path d="M0,300 C360,300 650,190 750,0 L820,0 L820,500 L0,500 Z" fill="var(--ink)"/>
    <path d="M0,318 C370,318 670,200 775,0 L820,0 L820,500 L0,500 Z" fill="var(--blue)"/>
  </svg>
  <svg class="band" viewBox="0 0 820 500" width="820" height="500" role="img" aria-label="Faint map of delivery routes in the blue band">
    <defs>
      <linearGradient id="mapTone" x1="0" y1="0" x2="1" y2="0">
        <stop offset="0" stop-color="#85acd3" stop-opacity="0"/>
        <stop offset="1" stop-color="#85acd3" stop-opacity=".16"/>
      </linearGradient>
    </defs>
    <path d="M0,318 C370,318 670,200 775,0 L820,0 L820,500 L0,500 Z" fill="url(#mapTone)"/>
  </svg>

  <div class="wordmark">Halvor Pinet</div>

  <div class="person">
    <span class="person__mark"></span>
    <div class="person__name">Dorian Vellacott</div>
    <div class="person__title">Manager</div>
  </div>

  <ul class="contacts">
    <li><svg viewBox="0 0 14 14"><path d="M7 0a5 5 0 0 0-5 5c0 4 5 9 5 9s5-5 5-9a5 5 0 0 0-5-5zm0 7a2 2 0 1 1 0-4 2 2 0 0 1 0 4z"/></svg>4, 18 Kestrel Road, Ferndale VIC 3190</li>
    <li><svg viewBox="0 0 14 14"><path d="M3 0l3 3-2 2c1 2 3 4 5 5l2-2 3 3-2 3C6 14 0 8 0 3z"/></svg>+61 3 9000 4172</li>
    <li><svg viewBox="0 0 14 14"><rect x="1" y="6" width="12" height="7" rx="1"/><path d="M0 5c2-4 12-4 14 0l-3 1-1-2H4L3 6z"/></svg>+61 3 9000 4172</li>
    <li><svg viewBox="0 0 14 14"><path d="M0 2h14v10H0z M1 3l6 5 6-5" stroke="#1d4f9c" stroke-width="1"/></svg>dvellacott@halvorpinet.com.au</li>
  </ul>

  <div class="web">
    <svg viewBox="0 0 14 14"><circle cx="7" cy="7" r="6" fill="none" stroke="#fff" stroke-width="1.4"/><path d="M1 7h12M7 1c3 3 3 9 0 12M7 1c-3 3-3 9 0 12" fill="none" stroke="#fff" stroke-width="1"/></svg>
    www.halvorpinet.com.au
  </div>

  <div class="tagline">Premium Suppliers of Real Time Temperature Tracking</div>
</section>

</body>
</html>
```